Tobin's Butter dairy product for export market

We are starting a new brand for our butter range. We are looking for a premimum branding with family values. The product should be elligent and simle and easy for consumers to choose and easy for chefs,

A samples of our current brand and packing details in on the pack
target markets , China, Hong Kong, Asia, middle east
products will be sold in different size starting from small portion eg 7g to 1kg food service pack
product will be sold in 2 varients salted and unsalted

Target Market(s)

Australian Market and export market

Industry/Entity Type

Product

Colors
9bcb3c
fbed22

Requirements
Must have
• Pure butter
• packed in Australia
• nice fresh modern simple design
Nice to have
• Colours gold , green or any other suggestions welcome.
Should not have
• Any third party pictures of butter etc..

```html
<!DOCTYPE html>
<html lang="en">
<head>
<meta charset="utf-8">
<title>Tobin's Butter – 1kg Pack Dieline</title>
<link href="https://fonts.googleapis.com/css2?family=Oswald:wght@500;700&family=Open+Sans:wght@400;600;700&display=swap" rel="stylesheet">
<style>
  :root{
    --bg:#ffffff;
    --fold:#6fc7a0;
    --measure:#4aa8d8;
    --green-dark:#1f5a24;
    --green-brand:#2e8b2e;
    --green-band:#8cc63f;
    --yellow:#fbed22;
    --yellow-deep:#f8d41c;
    --ink:#1f3a1f;
    --white:#ffffff;
  }
  html,body{margin:0;padding:0;overflow:hidden;background:var(--bg);}
  .canvas{width:1200px;height:1200px;display:block;}
  .measure-line{stroke:var(--measure);stroke-width:1;}
  .measure-label{fill:var(--measure);font-family:'Open Sans',sans-serif;font-size:12px;}
  .fold{stroke:var(--fold);stroke-width:1;fill:none;}
  .fold-dashed{stroke:var(--fold);stroke-width:1;fill:none;stroke-dasharray:4 4;}
  .dotted{stroke:var(--fold);stroke-width:1.5;fill:none;stroke-dasharray:1 7;}
  .date-code{fill:var(--measure);font-family:'Open Sans',sans-serif;font-size:30px;}
  .brand-name{fill:var(--green-dark);font-family:'Oswald',sans-serif;font-weight:700;}
  .pure-butter{fill:var(--green-dark);font-family:'Oswald',sans-serif;font-weight:700;font-size:60px;letter-spacing:-1px;}
  .variant{fill:var(--white);font-family:'Open Sans',sans-serif;font-size:21px;letter-spacing:1px;}
  .claims{fill:var(--green-dark);font-family:'Open Sans',sans-serif;font-size:14px;font-weight:600;}
  .net{fill:var(--ink);font-family:'Open Sans',sans-serif;font-size:19px;}
  .badge-caption{fill:var(--green-dark);font-family:'Open Sans',sans-serif;font-size:4.5px;font-weight:700;}
  .small-print{fill:var(--green-dark);font-family:'Open Sans',sans-serif;font-size:7.5px;}
  .ingredients{fill:var(--green-dark);font-family:'Open Sans',sans-serif;font-size:9px;}
  .table-cell{fill:var(--green-dark);font-family:'Open Sans',sans-serif;font-size:8px;}
  .table-line{stroke:var(--green-dark);stroke-width:.7;fill:none;}
</style>
</head>
<body>
<svg class="canvas" viewBox="0 0 1500 1500" xmlns="http://www.w3.org/2000/svg">
  <defs>
    <linearGradient id="goldSheet" x1="0" y1="0" x2="1" y2="1">
      <stop offset="0" stop-color="#d9a834"/>
      <stop offset=".35" stop-color="#ecd06a"/>
      <stop offset=".5" stop-color="#f4ea88"/>
      <stop offset=".75" stop-color="#e8c85a"/>
      <stop offset="1" stop-color="#d6a233"/>
    </linearGradient>
    <radialGradient id="frontGlow" cx=".3" cy=".4" r=".8">
      <stop offset="0" stop-color="#fffbc8"/>
      <stop offset=".5" stop-color="#fbed22"/>
      <stop offset="1" stop-color="#f0d34a"/>
    </radialGradient>
  </defs>

  <g class="measurements">
    <line class="measure-line" x1="177" y1="115" x2="177" y2="195"/>
    <line class="measure-line" x1="319" y1="130" x2="319" y2="160"/>
    <line class="measure-line" x1="878" y1="130" x2="878" y2="160"/>
    <line class="measure-line" x1="1020" y1="115" x2="1020" y2="195"/>
    <line class="measure-line" x1="177" y1="155" x2="1020" y2="155"/>
    <text class="measure-label" x="248" y="146" text-anchor="middle">44mm</text>
    <text class="measure-label" x="598" y="146" text-anchor="middle">172mm</text>
    <text class="measure-label" x="949" y="146" text-anchor="middle">44mm</text>
    <line class="measure-line" x1="1060" y1="195" x2="1100" y2="195"/>
    <text class="measure-label" transform="translate(1072,266) rotate(90)" text-anchor="middle">Flap<tspan x="0" dy="13">44mm</tspan></text>
    <text class="measure-label" transform="translate(1072,456) rotate(90)" text-anchor="middle">Side<tspan x="0" dy="13">80mm</tspan></text>
    <text class="measure-label" transform="translate(1072,718) rotate(90)" text-anchor="middle">Front<tspan x="0" dy="13">78mm</tspan></text>
  </g>

  <rect class="sheet" x="122" y="173" width="936" height="1107" fill="url(#goldSheet)"/>

  <g class="folds">
    <rect class="fold" x="177" y="195" width="843" height="1058"/>
    <line class="fold" x1="319" y1="195" x2="319" y2="1253"/>
    <line class="fold" x1="878" y1="195" x2="878" y2="1253"/>
    <line class="fold" x1="177" y1="338" x2="1020" y2="338"/>
    <line class="fold" x1="177" y1="598" x2="1020" y2="598"/>
    <line class="fold" x1="177" y1="851" x2="1020" y2="851"/>
    <line class="fold" x1="177" y1="1110" x2="1020" y2="1110"/>
    <line class="fold-dashed" x1="115" y1="338" x2="177" y2="338"/>
    <line class="fold-dashed" x1="115" y1="598" x2="177" y2="598"/>
    <line class="fold-dashed" x1="115" y1="851" x2="177" y2="851"/>
    <line class="fold-dashed" x1="115" y1="1253" x2="177" y2="1253"/>
    <line class="fold-dashed" x1="1020" y1="338" x2="1080" y2="338"/>
    <line class="fold-dashed" x1="1020" y1="598" x2="1080" y2="598"/>
    <line class="fold-dashed" x1="1020" y1="851" x2="1080" y2="851"/>
    <line class="fold-dashed" x1="319" y1="1253" x2="319" y2="1310"/>
    <line class="fold-dashed" x1="878" y1="1253" x2="878" y2="1310"/>
    <polyline class="fold" points="319,338 462,195"/>
    <polyline class="fold" points="878,338 748,195"/>
    <polyline class="fold" points="177,470 319,598"/>
    <polyline class="fold" points="1020,470 878,598"/>
    <polyline class="fold" points="177,980 319,851"/>
    <polyline class="fold" points="1020,980 878,851"/>
    <polyline class="fold" points="319,1110 448,1253"/>
    <polyline class="fold" points="878,1110 748,1253"/>
    <polygon class="fold" points="287,632 222,725 287,818"/>
    <polygon class="fold" points="911,632 975,725 911,818"/>
  </g>

  <g class="date-code-flap">
    <rect class="dotted" x="319" y="275" width="559" height="50"/>
    <text class="date-code" transform="rotate(180,580,297)" x="580" y="307" text-anchor="middle">Date Code Area</text>
  </g>

  <g class="side-panel" transform="rotate(180,598,468)">
    <rect class="fold-dashed" x="336" y="354" width="524" height="228"/>
    <g class="side-brand">
      <circle cx="496" cy="414" r="30" fill="var(--green-brand)"/>
      <text class="brand-name" x="536" y="414" font-size="30">Tobin's</text>
      <text class="brand-name" x="536" y="440" font-size="20">Butter</text>
    </g>
    <text class="ingredients" x="480" y="486"><tspan font-weight="700">INGREDIENTS:</tspan>
      <tspan x="480" dy="12">CREAM (FROM <tspan font-weight="700">MILK</tspan>),</tspan>
      <tspan x="480" dy="12">WATER, LACTIC ACID,</tspan>
      <tspan x="480" dy="12">STARTER DISTILLATE</tspan>
      <tspan x="480" dy="12"><tspan font-weight="700">MILK FAT:</tspan> 80% MIN</tspan>
      <tspan x="480" dy="12">PRODUCT OF AUSTRALIA</tspan>
      <tspan x="480" dy="12">STORE BELOW 4°C</tspan>
    </text>
    <g class="nutrition-table">
      <rect class="table-line" x="666" y="366" width="172" height="208"/>
      <line class="table-line" x1="666" y1="382" x2="838" y2="382"/>
      <line class="table-line" x1="666" y1="398" x2="838" y2="398"/>
      <line class="table-line" x1="666" y1="414" x2="838" y2="414"/>
      <line class="table-line" x1="666" y1="430" x2="838" y2="430"/>
      <line class="table-line" x1="666" y1="446" x2="838" y2="446"/>
      <line class="table-line" x1="666" y1="462" x2="838" y2="462"/>
      <line class="table-line" x1="666" y1="478" x2="838" y2="478"/>
      <line class="table-line" x1="666" y1="494" x2="838" y2="494"/>
      <line class="table-line" x1="666" y1="510" x2="838" y2="510"/>
      <line class="table-line" x1="666" y1="526" x2="838" y2="526"/>
      <line class="table-line" x1="666" y1="542" x2="838" y2="542"/>
      <line class="table-line" x1="666" y1="558" x2="838" y2="558"/>
      <line class="table-line" x1="736" y1="414" x2="736" y2="574"/>
      <line class="table-line" x1="790" y1="414" x2="790" y2="574"/>
      <text class="table-cell" x="670" y="377">NUTRITION INFORMATION</text>
      <text class="table-cell" x="670" y="393">SERVINGS PER PACK: 100</text>
      <text class="table-cell" x="670" y="409">SERVING SIZE: 10g</text>
      <text class="table-cell" x="670" y="425">Average Quantity</text>
      <text class="table-cell" x="740" y="425">Per serving</text><text class="table-cell" x="794" y="425">Per 100g</text>
      <text class="table-cell" x="670" y="441">Energy</text><text class="table-cell" x="740" y="441">302kJ</text><text class="table-cell" x="794" y="441">3020kJ</text>
      <text class="table-cell" x="670" y="457">Protein</text><text class="table-cell" x="740" y="457">Less than 1g</text><text class="table-cell" x="794" y="457">Less than 1g</text>
      <text class="table-cell" x="670" y="473">Fat(Total)</text><text class="table-cell" x="740" y="473">8.1g</text><text class="table-cell" x="794" y="473">81g</text>
      <text class="table-cell" x="670" y="489">– Saturated</text><text class="table-cell" x="740" y="489">5.4g</text><text class="table-cell" x="794" y="489">54g</text>
      <text class="table-cell" x="670" y="505">– Trans Fat</text><text class="table-cell" x="740" y="505">Less than 1g</text><text class="table-cell" x="794" y="505">4.0g</text>
      <text class="table-cell" x="670" y="521">Carbohydrates</text>
      <text class="table-cell" x="670" y="537">– Total</text><text class="table-cell" x="740" y="537">Less than 1g</text><text class="table-cell" x="794" y="537">Less than 1g</text>
      <text class="table-cell" x="670" y="553">– Sugars</text><text class="table-cell" x="740" y="553">Less than 1g</text><text class="table-cell" x="794" y="553">Less than 1g</text>
      <text class="table-cell" x="670" y="569">Sodium</text><text class="table-cell" x="740" y="569">Less than 1mg</text><text class="table-cell" x="794" y="569">5mg</text>
    </g>
  </g>

  <g class="front-panel" id="frontPanel">
    <rect x="319" y="598" width="559" height="253" fill="url(#frontGlow)"/>
    <rect x="600" y="640" width="270" height="168" fill="#f7e04a" opacity=".55" role="img" aria-label="Melted butter splash backdrop"/>
    <rect x="319" y="808" width="559" height="43" fill="var(--yellow-deep)"/>
    <rect class="fold-dashed" x="335" y="614" width="527" height="221"/>
    <text class="net" x="845" y="642" text-anchor="end">1kgNET</text>
    <circle cx="580" cy="660" r="34" fill="#d9c89a" opacity=".7"/>
    <g class="front-brand">
      <circle cx="400" cy="715" r="52" fill="var(--green-brand)"/>
      <text class="brand-name" x="462" y="712" font-size="44">Tobin's</text>
      <text class="brand-name" x="462" y="748" font-size="30">Butter</text>
    </g>
    <text class="pure-butter" x="606" y="708" textLength="247" lengthAdjust="spacingAndGlyphs">Pure Butter</text>
    <rect x="607" y="712" width="243" height="21" fill="var(--green-band)"/>
    <text class="variant" x="725" y="730" text-anchor="middle">UNSALTED</text>
    <text class="claims" x="725" y="761" text-anchor="middle">NO PRESERVATIVES</text>
    <text class="claims" x="725" y="778" text-anchor="middle">NO VEGETABLE FATS</text>
    <circle cx="702" cy="808" r="13" fill="var(--green-dark)" opacity=".85"/>
    <circle cx="754" cy="808" r="13" fill="var(--green-dark)" opacity=".85"/>
    <text class="badge-caption" x="702" y="829" text-anchor="middle">VEGETARIAN FRIENDLY</text>
    <text class="badge-caption" x="754" y="829" text-anchor="middle">HALAL CERTIFIED</text>
  </g>
  <use href="#frontPanel" transform="translate(0,253)"/>
  <rect x="319" y="1104" width="559" height="6" fill="var(--yellow-deep)"/>

  <rect x="1004" y="692" width="32" height="64" fill="#111"/>

  <g class="bottom-flap">
    <polygon class="fold-dashed" points="355,1127 840,1127 815,1205 380,1205"/>
    <text class="small-print" text-anchor="middle">
      <tspan x="598" y="1138">PACKED BY :</tspan>
      <tspan x="598" dy="8">SOUTHERN CREAMERY PTY LTD</tspan>
      <tspan x="598" dy="8">PHONE: +61 3 9000 4412  EMAIL: INFO@SOUTHERNCREAMERY.EXAMPLE</tspan>
      <tspan x="598" dy="8">12 HARBOUR LANE NEWPORT VICTORIA 3015 AUSTRALIA</tspan>
      <tspan x="598" dy="8">REG NO: 5817</tspan>
      <tspan x="598" dy="12">PRODUCED &amp; PACKED FOR :</tspan>
      <tspan x="598" dy="8">BELLFIELD TRADING PTY LTD</tspan>
      <tspan x="598" dy="8">4 ROWAN COURT EPPING VICTORIA 3076 AUSTRALIA</tspan>
    </text>
  </g>
</svg>
</body>
</html>
```